Bramwell Resources Ltd. - Refreshed business card challenge

A revised, refreshed business card design for my oil and gas company using my existing logo. Feel free to be as creative as you like!

Target Market(s)

bankers, lawyers

Industry/Entity Type

Oil And Gas Exploration

Contact Information for Business Card

See the "Must Haves" section

Font styles to use
Serif
Sans Serif

Colors

Designer to choose colors to be used in the design.

Requirements
Must have
• Existing business logo, name, title, email, phone number, business address
• Neil Hadley, CA, CPA
• Vice President Finance & Chief Financial Officer
• nhadley@bramwellresources-mail.com
• office: (587)555-0142
• cell: (403)555-0187
• 1400, 815 4 Street S.W.
• Calgary, AB
• T2P 4K8
Should not have
• Should not be plain and boring.

```html
<!DOCTYPE html>
<html lang="en">
<head>
<meta charset="utf-8">
<title>Bramwell Resources – Business Card</title>
<link href="https://fonts.googleapis.com/css2?family=Montserrat:wght@400;700;800&display=swap" rel="stylesheet">
<style>
  :root {
    --stage: #4a4a4c;
    --card-dark: #070707;
    --card-light: #ffffff;
    --mark-dark: #5a5a5a;
    --green: #0f4d36;
    --brown: #6b3a24;
  }
  * { box-sizing: border-box; margin: 0; padding: 0; }
  html, body { width: 1200px; height: 960px; overflow: hidden; }
  body {
    background: var(--stage);
    font-family: "Montserrat", sans-serif;
    position: relative;
  }
  .card {
    position: absolute;
    left: 220px;
    width: 760px;
    height: 434px;
    overflow: hidden;
    box-shadow: 0 10px 30px rgba(0,0,0,.35);
  }
  .card--back { top: 30px; background: var(--card-dark); }
  .card--front { top: 496px; background: var(--card-light); }

  .brand {
    position: absolute;
    display: flex;
    align-items: center;
    gap: 12px;
    font-weight: 800;
    line-height: 1.05;
    letter-spacing: .5px;
  }
  .brand__dot { width: 22px; height: 22px; border-radius: 50%; flex: none; }
  .card--back .brand { left: 230px; top: 180px; font-size: 38px; color: var(--mark-dark); }
  .card--back .brand__dot { background: var(--mark-dark); }
  .card--front .brand { left: 60px; top: 240px; font-size: 30px; color: var(--green); }
  .card--front .brand__dot { background: var(--green); }

  .divider {
    position: absolute;
    left: 340px; top: 130px;
    width: 2px; height: 170px;
    background: linear-gradient(to bottom, rgba(15,77,54,0), var(--green) 50%, rgba(15,77,54,0));
  }
  .details {
    position: absolute;
    left: 374px; top: 92px;
    width: 346px;
    color: var(--brown);
  }
  .details__name { font-weight: 700; font-size: 23px; color: var(--green); white-space: nowrap; }
  .details__title { font-size: 15.5px; line-height: 1.35; margin-top: 4px; }
  .details__address { font-size: 15.5px; line-height: 1.35; margin-top: 18px; }
  .contact { list-style: none; margin-top: 18px; font-size: 15.5px; line-height: 1.5; }
  .contact li { display: flex; align-items: center; gap: 10px; white-space: nowrap; }
  .contact svg { width: 15px; height: 15px; flex: none; fill: var(--green); }
</style>
</head>
<body>
  <section class="card card--back" aria-label="Card back">
    <div class="brand"><span class="brand__dot"></span><span>Bramwell<br>Resources</span></div>
  </section>

  <section class="card card--front" aria-label="Card front">
    <div class="brand"><span class="brand__dot"></span><span>Bramwell<br>Resources</span></div>
    <div class="divider"></div>
    <div class="details">
      <p class="details__name">Neil Hadley, CA, CPA</p>
      <p class="details__title">Vice President Finance &amp;<br>Chief Financial Officer</p>
      <p class="details__address">1400, 815 4 Street S.W.<br>Calgary, AB T2P 4K8</p>
      <ul class="contact">
        <li><svg viewBox="0 0 16 16" aria-hidden="true"><path d="M3.5 1.5l2.5 0 1 3.5-1.6 1.2a8 8 0 0 0 4.4 4.4L11 9l3.5 1v2.5c0 1-1 2-2 2A11 11 0 0 1 1.5 3.5c0-1 1-2 2-2z"/></svg>(587)555-0142</li>
        <li><svg viewBox="0 0 16 16" aria-hidden="true"><path d="M4.5 1h7a1 1 0 0 1 1 1v12a1 1 0 0 1-1 1h-7a1 1 0 0 1-1-1V2a1 1 0 0 1 1-1zm.5 2v9h6V3zm3 10a.8.8 0 1 0 0 1.6.8.8 0 0 0 0-1.6z"/></svg>(403)555-0187</li>
        <li><svg viewBox="0 0 16 16" aria-hidden="true"><path d="M1 3h14v10H1zm1.5 1.2v.3L8 8.6l5.5-4.1v-.3zm0 2.1v5.5h11V6.3L8 10.4z"/></svg>nhadley@bramwellresources-mail.com</li>
      </ul>
    </div>
  </section>
</body>
</html>
```